Creative Brief
Cedar Brook Emergency Center
Web Site
Health
www.CedarBrookER.example
We are the first Free Standing Emergency Room in Dallas! We have all the advantages of a hospital based ER without the hassle or wait. Add in customer service and a aesthetic environment and you will see what makes us so unique for you emergent medical needs.
Our free standing ER solution provides
No wait emergency rooms!
Open 24 hours a day, 7 days a week
State of the art equipment and diagnosing capabilities
All our doctors are trained Emergency Medicine physicians
Experienced friendly nurses
Onsite emergent radiology (x-rays, CAT scans, Ultrasound)
Onsite emergent laboratory with result within minutes
I like a clean website- not too busy. Needs to be professional. A few nice pictures representing emergency medicine. I do not want things that are overused like pictures of a heart or EKG strip. Please incorporate the logo and from the logo you can see they colors and fonts that I like
left side
I do not have any specific web sites that i like or dislike and am open to many options.
web content

```html
<!DOCTYPE html>
<html lang="en">
<head>
<meta charset="utf-8">
<title>Cedar Brook Emergency Center</title>
<link href="https://fonts.googleapis.com/css2?family=Open+Sans:wght@300;400;600;700&family=Cinzel:wght@700&display=swap" rel="stylesheet">
<style>
:root{
  --red:#b3141b;
  --red-dark:#8c0d12;
  --ink:#3a3a3a;
  --muted:#7a7a7a;
  --line:#d6d6d6;
  --page:#e9e9e9;
  --white:#ffffff;
}
*{box-sizing:border-box;margin:0;padding:0}
html,body{width:1200px;height:1083px;overflow:hidden}
body{background:var(--page);font-family:"Open Sans",Arial,sans-serif;color:var(--ink);position:relative}
.abs{position:absolute}

.header{left:0;top:0;width:1200px;height:128px;background:linear-gradient(#ffffff,#f1f1f1)}
.brand{left:160px;top:22px;display:flex;align-items:center;gap:16px}
.brand-dot{width:80px;height:80px;border-radius:50%;background:var(--red)}
.brand-name{font-family:"Cinzel",serif;font-weight:700;color:var(--red);font-size:38px;line-height:1.05;letter-spacing:1px}
.brand-name small{display:block;font-size:20px;letter-spacing:5px}
.contact-box{left:880px;top:26px;width:250px;text-align:right}
.contact-label{font-size:11px;color:var(--muted);letter-spacing:1px}
.contact-phone{font-size:30px;font-weight:700;color:var(--ink);line-height:1.1}
.contact-addr{font-size:12px;color:var(--muted);line-height:1.35}

.nav{left:0;top:128px;width:1200px;height:42px;background:#f7f7f7;border-top:1px solid var(--line);border-bottom:1px solid var(--line)}
.nav ul{list-style:none;display:flex;position:absolute;left:175px;top:0;height:42px}
.nav li{font-size:15px;padding:0 18px;line-height:42px;color:var(--ink);border-right:1px solid var(--line)}
.nav li.active{background:var(--red);color:var(--white);border-radius:4px 4px 0 0;height:32px;line-height:32px;margin-top:10px}
.social{right:140px;top:139px;display:flex;gap:12px}
.social span{width:22px;height:22px;border-radius:50%;background:#9a9a9a}

.hero{left:0;top:170px;width:1200px;height:240px;background:linear-gradient(#cfcfcf,#f2f2f2 60%,#e2e2e2)}
.hero-photo{left:205px;top:175px;width:440px;height:235px;background:linear-gradient(160deg,#c9b7a4,#6f9a8c 55%,#e8e8e8)}
.hero-title{left:675px;top:215px;width:360px;text-align:right;font-weight:300;color:var(--red);line-height:1}
.hero-title .l1{font-size:40px}
.hero-title .l2{font-size:66px;color:var(--red-dark)}
.hero-title .l3{font-size:15px;letter-spacing:2px;color:var(--muted);margin-top:6px}
.dots{left:760px;top:364px;display:flex;gap:10px}
.dots span{width:16px;height:16px;border-radius:50%;background:#b9b9b9}
.dots span.on{background:var(--red-dark)}

.features{left:140px;top:410px;width:920px;height:82px;background:linear-gradient(var(--red),var(--red-dark));display:flex;align-items:center;justify-content:space-around;padding:0 20px}
.feature{display:flex;align-items:center;gap:10px;color:var(--white);font-size:13px;font-weight:700;line-height:1.2;width:170px}
.feature svg{flex:none}

.main{left:140px;top:498px;width:920px;height:497px;background:var(--white);box-shadow:0 1px 3px rgba(0,0,0,.15)}
.opening{left:175px;top:530px;color:var(--red)}
.opening h1{font-size:44px;font-weight:700;line-height:1.05}
.opening h2{font-size:36px;font-weight:400;line-height:1.1}
.story-photo{left:181px;top:620px;width:302px;height:185px;background:linear-gradient(180deg,#9fb3c4,#5f8a82 60%,#7d7d7d)}
.copy{font-size:13px;line-height:1.35;color:var(--muted)}
.copy-side{left:497px;top:618px;width:235px}
.copy-side p+p{margin-top:14px}
.copy-full{left:181px;top:818px;width:551px}
.copy-full p+p{margin-top:12px}
.divider{left:748px;top:530px;width:1px;height:440px;background:var(--line)}

.side-h{font-size:38px;font-weight:300;color:var(--red)}
.map-h{left:762px;top:528px}
.map{left:762px;top:597px;width:275px;height:140px;background:linear-gradient(135deg,#e6e2d2,#cfd8c4);border:1px solid var(--line)}
.ask-h{left:762px;top:762px}
.form{left:762px;top:822px;width:275px;height:150px;background:#e4e4e4;padding:12px 10px}
.field{display:flex;align-items:center;gap:8px;height:26px;margin-bottom:10px;background:var(--white);border:1px solid var(--line)}
.field i{width:22px;height:24px;background:var(--red-dark)}
.field span{font-size:11px;color:#a0a0a0}
.send{position:absolute;right:10px;bottom:8px;background:var(--red);color:var(--white);font-size:13px;padding:2px 10px}

.footer{left:0;top:1005px;width:1200px;height:78px;background:#dcdcdc;border-top:1px solid #c8c8c8}
.footer ul{list-style:none;display:flex;position:absolute;left:170px;top:26px}
.footer li{font-size:14px;padding:0 16px;border-right:1px solid #aaa;line-height:18px}
.footer li:last-child{border-right:none}
.footer-brand{right:140px;top:18px;display:flex;align-items:center;gap:10px}
.footer-brand .dot{width:40px;height:40px;border-radius:50%;background:#8f8f8f}
.footer-brand .name{font-family:"Cinzel",serif;font-weight:700;color:#6f6f6f;font-size:19px;line-height:1.05}
.footer-brand .name small{display:block;font-size:10px;letter-spacing:3px}
</style>
</head>
<body>
<header class="header abs">
  <div class="brand abs">
    <span class="brand-dot"></span>
    <div class="brand-name">CEDAR BROOK<small>EMERGENCY CENTER</small></div>
  </div>
  <div class="contact-box abs">
    <div class="contact-label">EMERGENCY CALL</div>
    <div class="contact-phone">(555) 014-2290</div>
    <div class="contact-addr">4410 Ridge Lane<br>Dallas<br>TX 75201</div>
  </div>
</header>

<nav class="nav abs">
  <ul>
    <li>Home</li><li>Services</li><li>About Us</li><li class="active">FAQ</li><li>Ask Doctor</li><li>Contact</li>
  </ul>
</nav>
<div class="social abs"><span></span><span></span><span></span></div>

<section class="hero abs"></section>
<div class="hero-photo abs" role="img" aria-label="Photo of a smiling emergency care team in scrubs and white coats"></div>
<div class="hero-title abs">
  <div class="l1">Experienced</div>
  <div class="l2">Friendly</div>
  <div class="l3">EMERGENCY TEAM</div>
</div>
<div class="dots abs"><span></span><span></span><span class="on"></span><span></span></div>

<section class="features abs">
  <div class="feature">
    <svg width="34" height="34" viewBox="0 0 34 34"><rect x="1" y="1" width="32" height="32" rx="3" fill="none" stroke="#fff" stroke-width="2"/><path d="M13 7h8v6h6v8h-6v6h-8v-6H7v-8h6z" fill="#fff"/></svg>
    <span>No Wait<br>Emergency<br>Rooms</span>
  </div>
  <div class="feature">
    <svg width="34" height="34" viewBox="0 0 34 34"><circle cx="17" cy="17" r="15" fill="none" stroke="#fff" stroke-width="2.5"/><path d="M17 8v9l6 4" stroke="#fff" stroke-width="2.5" fill="none"/></svg>
    <span>Open<br>24 hours a day,<br>7 days a week</span>
  </div>
  <div class="feature">
    <svg width="34" height="34" viewBox="0 0 34 34"><circle cx="17" cy="11" r="7" fill="#fff"/><path d="M4 33c0-9 6-13 13-13s13 4 13 13z" fill="#fff"/></svg>
    <span>Experienced<br>friendly<br>nurses</span>
  </div>
  <div class="feature">
    <svg width="34" height="34" viewBox="0 0 34 34"><rect x="3" y="3" width="28" height="28" rx="3" fill="none" stroke="#fff" stroke-width="2.5"/><path d="M17 7v20M10 12h14M10 17h14M10 22h14" stroke="#fff" stroke-width="2"/></svg>
    <span>Onsite<br>emergent<br>radiology</span>
  </div>
  <div class="feature">
    <svg width="34" height="34" viewBox="0 0 34 34"><path d="M13 3h8M15 3v10L6 30h22L19 13V3" fill="none" stroke="#fff" stroke-width="2.5"/><path d="M10 24h14l3 6H7z" fill="#fff"/></svg>
    <span>Onsite<br>emergent<br>laboratory</span>
  </div>
</section>

<main class="main abs"></main>
<div class="opening abs">
  <h1>Opening soon!</h1>
  <h2>look for us to open winter 2011</h2>
</div>
<div class="story-photo abs" role="img" aria-label="Photo of medical staff walking in front of the emergency center building"></div>
<div class="copy copy-side abs">
  <p>We are the first Free Standing Emergency Room in Dallas! We have all the advantages of a hospital based ER without the hassle or wait. Add in customer service and a aesthetic environment and you will see what makes us so unique for you emergent medical needs.</p>
  <p>Our doors stay open day and night.</p>
</div>
<div class="copy copy-full abs">
  <p>Modern imaging and a full laboratory sit on site, so answers come fast and you can return home sooner with a clear plan and follow up support from our friendly staff.</p>
  <p>Parking is right by the door and the waiting room stays quiet and clean. Children and adults are welcome, and we accept most insurance plans. Call ahead or simply walk in.</p>
</div>
<div class="divider abs"></div>

<h3 class="side-h map-h abs">Location Map</h3>
<div class="map abs" role="img" aria-label="Street map showing the emergency center location"></div>
<h3 class="side-h ask-h abs">Ask The Doctor</h3>
<form class="form abs">
  <div class="field"><i></i><span>Your name</span></div>
  <div class="field"><i></i><span>Your email</span></div>
  <div class="field"><i></i><span>Your question</span></div>
  <span class="send">Send</span>
</form>

<footer class="footer abs">
  <ul><li>Home</li><li>Services</li><li>About Us</li><li>FAQ</li><li>Ask Doctor</li><li>Contact</li></ul>
  <div class="footer-brand abs">
    <span class="dot"></span>
    <div class="name">CEDAR BROOK<small>EMERGENCY CENTER</small></div>
  </div>
</footer>
</body>
</html>
```